VELMAR WEBSITE

need to create a new website for VELMAR ltd
the company deals with all aspects of safety products & safety wear
we need a simple website to show
ideas can be taken from following website whose products we shall distribute in kenya
www.qtw.co.uk
www.brovik.eu
www.tormanhardgear.com
www.qalvenworks.co.za

we need following tabs
1) home - basic company information
2) products - broken down to following categories ie gloves, head protection, ear protection, mouth protection, foot protection
3) contacts

the company profile is a reputable company dealing with all aspects of safety, HSE (health and safety equipment), and PPE (personal protective equipment)

the website should have the brovik logo for which we are an authorized distributor.
the brovi industrial range writeup can be picked from their website

Dear Designers, i shall be able to choose a final design in 2 weeks, sorry i have not been able to finalise this due to a personal reason

Target Market(s)

the buyers are all types of industry who care for their employees safety

Industry/Entity Type

Industrial

Requirements
Must have
• clean look, fresh look, user freindly
Nice to have
• clear images, quick links etc

```html
<!DOCTYPE html>
<html lang="en">
<head>
<meta charset="utf-8">
<title>VELMAR – Safety Products</title>
<link href="https://fonts.googleapis.com/css2?family=Titillium+Web:wght@300;400;600;700&display=swap" rel="stylesheet">
<style>
:root{
  --slate:#263640;
  --slate-2:#1d2a32;
  --gold:#e9ae1f;
  --gold-light:#f3c640;
  --gold-text:#d99c12;
  --ink:#1b1b1b;
  --grey:#6b6b6b;
  --light-grey:#9a9a9a;
  --line:#dcdcdc;
  --page:#f3f3f3;
  --white:#ffffff;
  --teal:#17658a;
}
*{box-sizing:border-box;margin:0;padding:0}
html,body{width:1020px;height:1200px;overflow:hidden}
body{font-family:"Titillium Web",sans-serif;background:var(--page);position:relative;color:var(--ink)}
.abs{position:absolute}
.top-band{left:0;top:0;width:1020px;height:120px;background:var(--slate)}
.mid-band{left:0;top:120px;width:1020px;height:366px;background:var(--slate-2)}
.sheet{left:84px;top:0;width:865px;height:1081px;background:var(--white)}
/* header */
.brand{left:125px;top:34px;display:flex;align-items:center;gap:10px}
.brand-mark{width:34px;height:34px;background:var(--gold)}
.brand-name{font-size:34px;font-weight:700;color:var(--slate);letter-spacing:1px}
.account-links{right:97px;top:9px;font-size:11.5px;color:var(--grey);display:flex;align-items:center;gap:5px}
.account-links .sep{color:#bbb}
.cart{width:18px;height:16px}
.call-label{right:97px;top:63px;font-size:14.5px;color:#333}
.phone{right:97px;top:80px;font-size:23px;line-height:1;color:var(--slate);white-space:nowrap}
.social{left:694px;top:84px;display:flex;gap:8px}
.social span{width:18px;height:18px;display:block}
.social .s1{background:#3b5a98}.social .s2{background:#4fb5e6}.social .s3{background:#1d6ea8}
/* nav */
.main-nav{left:84px;top:120px;width:865px;height:41px;background:linear-gradient(#f1bf33,#e4a617);display:flex;align-items:center;padding-left:15px}
.main-nav a{color:var(--white);text-decoration:none;font-size:15.5px;padding:0 14px;line-height:41px;border-right:1px solid rgba(160,100,0,.45)}
.main-nav a:first-child{padding-left:7px}
.main-nav a:last-child{border-right:none}
/* hero */
.hero{left:85px;top:161px;width:864px;height:325px;background:linear-gradient(180deg,#8fbfe4 0%,#b9d6ea 40%,#6f7a6e 75%,#3a3e3a 100%)}
.hero-caption{left:567px;top:311px;width:350px;height:126px;background:rgba(45,62,72,.95);border-top:4px solid var(--gold);padding:20px 27px}
.hero-caption h2{font-weight:400;font-size:26.5px;color:var(--white);line-height:1.1;white-space:nowrap;margin-left:-1px}
.hero-caption p{font-size:13.5px;color:#e6e6e6;line-height:22px;margin-top:4px}
.dots{left:485px;top:464px;display:flex;gap:5px}
.dots span{width:12px;height:12px;border-radius:50%;background:#333}
.dots span:first-child{background:#9a9a9a}
/* welcome */
.welcome{left:114px;top:516px;width:560px}
.welcome h1{font-weight:400;font-size:21.5px;letter-spacing:.2px}
.welcome .lead{font-size:13.5px;color:var(--grey);margin-top:4px}
.welcome .body{font-size:11.3px;color:var(--grey);line-height:21px;margin-top:2px}
.divider{left:116px;top:657px;width:550px;border-top:1px dotted #bbb}
.section-title{left:116px;top:675px;font-size:19.5px;color:var(--gold-text);font-weight:400}
/* products */
.product-card{width:175px;height:170px;border:1px solid var(--line);border-radius:3px;background:var(--white);text-align:center}
.product-card .photo{width:80px;height:86px;margin:9px auto 0;border-radius:8px}
.product-card h3{font-weight:400;font-size:13.5px;margin-top:11px}
.product-card p{font-size:10.5px;color:var(--light-grey);line-height:15px;padding:0 12px}
/* sidebar */
.side-box{left:694px;width:241px;border:1px solid var(--line);border-radius:4px}
.category{top:507px;height:110px;background:linear-gradient(#fff 60%,#f0f0f0);padding:14px 22px}
.category h2{font-weight:400;font-size:19px;color:var(--slate)}
.category p{font-size:10.5px;color:var(--grey);line-height:15px;margin-top:1px}
.btn{display:inline-block;margin-top:6px;background:var(--slate-2);color:var(--white);font-size:9.5px;padding:5px 15px;border-radius:2px}
.why{top:624px;height:139px;border:1px solid #d9a21a;background:linear-gradient(#f3c84a,#e6a71a);padding:16px 22px}
.why h2{font-weight:400;font-size:16px;color:var(--white);line-height:1}
.why h2 strong{display:block;font-size:22px;font-weight:700;letter-spacing:.5px;margin-top:2px}
.why p{font-size:10.5px;color:var(--white);line-height:17px;margin-top:8px}
.news{top:771px;height:284px;background:var(--white)}
.news h2{font-weight:400;font-size:19px;color:var(--slate);padding:11px 23px;height:41px;background:linear-gradient(#fff,#f3f3f3);border-bottom:1px solid var(--line)}
.news-item{display:flex;gap:8px;padding:0 0 0 22px;height:73px;align-items:flex-start}
.news-item:first-of-type{margin-top:14px}
.news-item .thumb{width:76px;height:57px;flex:none}
.news-item .text{width:125px}
.news-item h3{font-weight:400;font-size:12px;color:var(--ink);margin-top:-1px}
.news-item p{font-size:10px;color:var(--light-grey);line-height:15px}
/* footer */
.footer{left:0;top:1081px;width:1020px;height:119px;background:var(--white);border-top:1px solid #e8e8e8}
.footer-links{left:99px;top:1113px;font-size:13px;color:#444;display:flex;gap:5px}
.footer-links .sep{color:#888}
.copyright{left:100px;top:1139px;font-size:11.5px;color:var(--grey)}
.partner{left:775px;top:1100px;font-size:46px;font-weight:700;color:var(--teal)}
</style>
</head>
<body>
<div class="abs top-band"></div>
<div class="abs mid-band"></div>
<div class="abs sheet"></div>

<header>
  <div class="abs brand"><span class="brand-mark"></span><span class="brand-name">VELMAR</span></div>
  <div class="abs account-links">
    <span>My Account</span><span class="sep">|</span><span>Login</span><span class="sep">|</span><span>Register</span><span class="sep">|</span><span>My Cart</span>
    <svg class="cart" viewBox="0 0 18 16"><path d="M1 2h3l2 8h9l2-6H5" fill="none" stroke="#222" stroke-width="1.5"/><circle cx="7" cy="13.5" r="1.5" fill="#222"/><circle cx="14" cy="13.5" r="1.5" fill="#222"/></svg>
  </div>
  <div class="abs call-label">CALL US NOW</div>
  <div class="abs phone">0800 555 0134</div>
  <div class="abs social"><span class="s1"></span><span class="s2"></span><span class="s3"></span></div>
</header>

<nav class="abs main-nav">
  <a href="#">HOME</a><a href="#">ABOUT US</a><a href="#">PRODUCTS</a><a href="#">SERVICES</a><a href="#">PARTNERS</a><a href="#">ORDER NOW</a><a href="#">SUPPORT</a><a href="#">CONTACT</a>
</nav>

<section>
  <div class="abs hero" role="img" aria-label="Site workers in hard hats and high-visibility vests beside a crane"></div>
  <div class="abs hero-caption">
    <h2>We Deliver Safety Products</h2>
    <p>Class aptent taciti sociosqu ad litora torquent per conubia nostra, per inceptos hymenaeos.</p>
  </div>
  <div class="abs dots"><span></span><span></span><span></span><span></span></div>
</section>

<main>
  <div class="abs welcome">
    <h1>WELCOME TO VELMAR WEBSITE MAINPAGE</h1>
    <p class="lead">Duis tincidunt lectus quis dui viverra vestibulum. Suspendisse vulputate aliquam dui.</p>
    <p class="body">Nulla elementum dui ut augue. Aliquam vehicula mi at mauris. Maecenas placerat, nisl at consequat rhoncus, sem nunc gravida justo, quis eleifend arcu velit quis lacus. Morbi magna magna, tincidunt a, mattis non, imperdiet vitae, tellus. Sed odio est, auctor ac, sollicitudin in, consequat vitae, orci. Fusce id felis.</p>
  </div>
  <div class="abs divider"></div>
  <h2 class="abs section-title">OUR PRODUCTS</h2>

  <div class="abs product-card" style="left:117px;top:707px"><div class="photo" role="img" aria-label="Welding helmet" style="background:linear-gradient(#4a4f6a,#1e2030)"></div><h3>PRODUCT NAME</h3><p>Morbi magna magna tincidunt a mattis non imperdiet</p></div>
  <div class="abs product-card" style="left:297px;top:707px"><div class="photo" role="img" aria-label="Safety goggles" style="background:linear-gradient(#d9e6f2,#8fb0d4)"></div><h3>PRODUCT NAME</h3><p>Morbi magna magna tincidunt a mattis non imperdiet</p></div>
  <div class="abs product-card" style="left:479px;top:707px"><div class="photo" role="img" aria-label="Dust masks" style="background:linear-gradient(#ffffff,#e2e2e2)"></div><h3>PRODUCT NAME</h3><p>Morbi magna magna tincidunt a mattis non imperdiet</p></div>
  <div class="abs product-card" style="left:117px;top:885px"><div class="photo" role="img" aria-label="Safety harness" style="background:linear-gradient(#f3b9a3,#e0603a)"></div><h3>PRODUCT NAME</h3><p>Morbi magna magna tincidunt a mattis non imperdiet</p></div>
  <div class="abs product-card" style="left:297px;top:885px"><div class="photo" role="img" aria-label="Work glove" style="background:linear-gradient(#4c67c9,#1f2c6b)"></div><h3>PRODUCT NAME</h3><p>Morbi magna magna tincidunt a mattis non imperdiet</p></div>
  <div class="abs product-card" style="left:479px;top:885px"><div class="photo" role="img" aria-label="Gas detector" style="background:linear-gradient(#f7dc3a,#e3b81a)"></div><h3>PRODUCT NAME</h3><p>Morbi magna magna tincidunt a mattis non imperdiet</p></div>

  <aside>
    <div class="abs side-box category">
      <h2>VIEW OUR CATEGORY</h2>
      <p>Suspendisse vulputate aliquam dui. Nulla elementum dui ut augue.</p>
      <span class="btn">VIEW MORE</span>
    </div>
    <div class="abs side-box why">
      <h2>WHY CHOOSE OUR <strong>PRODUCTS</strong></h2>
      <p>Morbi eget arcu. Morbi porta, libero id ullamcorper nonummy, nibh ligula pulvinar metus, eget consv et scelerisque mi</p>
    </div>
    <div class="abs side-box news">
      <h2>LATEST NEWS</h2>
      <div class="news-item"><div class="thumb" role="img" aria-label="Warehouse worker among shelves" style="background:linear-gradient(#8a7a6a,#b8473a)"></div><div class="text"><h3>NEWS TITTLE HERE</h3><p>Suspendisse vulputate<br>aliquam dui Nulla elemen</p></div></div>
      <div class="news-item"><div class="thumb" role="img" aria-label="Worker with safety equipment outdoors" style="background:linear-gradient(#6f9bd0,#2f3238)"></div><div class="text"><h3>NEWS TITTLE HERE</h3><p>Suspendisse vulputate<br>aliquam dui Nulla elemen</p></div></div>
      <div class="news-item"><div class="thumb" role="img" aria-label="Worker in hard hat and orange vest" style="background:linear-gradient(#c9a25a,#e07a2a)"></div><div class="text"><h3>NEWS TITTLE HERE</h3><p>Suspendisse vulputate<br>aliquam dui Nulla elemen</p></div></div>
    </div>
  </aside>
</main>

<footer>
  <div class="abs footer"></div>
  <div class="abs footer-links">
    <span>HOME</span><span class="sep">|</span><span>ABOUT US</span><span class="sep">|</span><span>PRODUCTS</span><span class="sep">|</span><span>SERVICES</span><span class="sep">|</span><span>PARTNERS</span><span class="sep">|</span><span>ORDER NOW</span><span class="sep">|</span><span>SUPPORT</span><span class="sep">|</span><span>CONTACT</span>
  </div>
  <div class="abs copyright">Copyright © 2013 Company Name.&nbsp; All right reserved</div>
  <div class="abs partner">Brovik</div>
</footer>
</body>
</html>
```